Accountant services flyer & marketing portfolio

I require a design for a marketing portfolio of blank templates for a flyer, product brochure, report cover for A4 based on our style - current logo, letterhead, website look and feel - that can be updated in publisher or word with relevant marketing and company information editorial material and text. It will be either printed A4 or saved as PDF and distributed

Target Market(s)

small business and investment / superfund clients

Industry/Entity Type

Accountant

Font styles to use
Sans Serif

Requirements
Must have
• Instyle of letterhead and website
Professional body logos
Space to input text
Relevant happy images
Nice to have
• Images of happy lifestyle types retirees, young families and mid-aged
tradesmen and professionals

```html
<!DOCTYPE html>
<html lang="en">
<head>
<meta charset="utf-8">
<title>Meridian Advisory – Flyer</title>
<link href="https://fonts.googleapis.com/css2?family=Arimo:wght@400;700&family=Barlow+Condensed:wght@300;400;600&display=swap" rel="stylesheet">
<style>
  :root{
    --orange:#f15a24;
    --black:#000;
    --brown:#4a1a0e;
    --ink:#333;
    --backdrop:#b1b2b4;
    --paper:#fff;
    --badge:#d9dde3;
  }
  *{margin:0;padding:0;box-sizing:border-box}
  html,body{width:1200px;height:1200px;overflow:hidden;background:var(--backdrop)}
  body{font-family:Arimo,Arial,sans-serif;color:var(--ink)}
  .flyer{position:absolute;left:231px;top:78px;width:738px;height:1044px;background:var(--paper);overflow:hidden}
  .brand{position:absolute;left:27px;top:70px}
  .brand-name{font-size:19px;font-weight:700;color:var(--orange);letter-spacing:-.2px;white-space:nowrap}
  .brand-tagline{font-size:11.5px;color:#222;margin-top:3px}
  .contacts{position:absolute;left:538px;top:36px;list-style:none;font-size:11px;color:#333}
  .contacts li{display:flex;align-items:center;height:18px}
  .contacts .dot{width:10px;height:10px;border-radius:50%;background:var(--orange);margin-right:8px;flex:none}
  .hero-photo{position:absolute;left:0;top:116px;width:738px;height:365px;
    background:linear-gradient(100deg,#2f5fa8 0%,#5a7fc4 25%,#b7b8e6 50%,#e7c3de 72%,#f7a7a3 88%,#f5866e 100%)}
  .banner{position:absolute;left:0;top:426px;width:738px;height:196px}
  .banner svg{position:absolute;left:0;top:0}
  .headline{position:absolute;left:39px;top:80px;font-family:"Barlow Condensed",sans-serif;font-weight:600;font-size:32px;line-height:35px;color:#fff;text-transform:uppercase}
  .slogan{position:absolute;right:34px;top:60px;text-align:right;font-family:"Barlow Condensed",sans-serif;color:#fff;text-transform:uppercase;font-weight:300}
  .slogan .big{font-size:44px;line-height:44px}
  .slogan .small{font-size:24px}
  .slogan .mid{font-size:25px;line-height:30px}
  .slogan b{font-weight:600}
  .column{position:absolute;top:642px;width:156px;font-size:10.8px;line-height:12.5px}
  .column h2{font-size:13.2px;line-height:15.4px;font-weight:700;margin-bottom:3px}
  .column p{margin-bottom:12.5px}
  .col-1{left:80px}.col-2{left:313px}.col-3{left:541px}
  .icon{position:absolute}
  .badge{position:absolute;background:var(--badge)}
  .legal{position:absolute;left:528px;top:987px;width:210px;height:57px;background:var(--orange);color:#fff;padding:7px 12px;font-size:8.4px;line-height:10.5px}
  .legal i{display:block}
  .legal b{display:block;margin-top:6px}
  .base-bar{position:absolute;left:0;top:1032px;width:528px;height:12px;background:var(--black)}
</style>
</head>
<body>
<main class="flyer">
  <header>
    <div class="brand">
      <div class="brand-name">MERIDIAN ADVISORY</div>
      <div class="brand-tagline">Clear advice. Confident futures</div>
    </div>
    <ul class="contacts">
      <li><span class="dot"></span>1300 555 014</li>
      <li><span class="dot"></span>612 5550 1873</li>
      <li><span class="dot"></span>hello@meridianadvisory.example</li>
      <li><span class="dot"></span>www.meridianadvisory.example</li>
    </ul>
  </header>

  <div class="hero-photo" role="img" aria-label="Photo of hands typing on a laptop overlaid with rising financial bar and line charts, blue to pink tones"></div>

  <section class="banner">
    <svg width="738" height="196" viewBox="0 0 738 196">
      <polygon points="0,67 480,67 418,196 0,196" fill="var(--orange)"/>
      <polygon points="511,0 738,0 738,196 418,196" fill="var(--black)"/>
      <polygon points="480,67 582,67 418,196" fill="var(--brown)"/>
    </svg>
    <h1 class="headline">Lorem ipsum dolor sitamet<br>dolorconsectetur adipiscing<br>semper justo vitae laoreet.</h1>
    <div class="slogan">
      <div class="big"><span class="small">The</span> Digital</div>
      <div class="mid"><b>Revolution</b> has begun ...</div>
      <div class="mid">Embrace the opportunity!</div>
    </div>
  </section>

  <svg class="icon" style="left:40px;top:643px" width="34" height="40" viewBox="0 0 34 40" fill="none" stroke="var(--orange)" stroke-width="2">
    <rect x="3" y="2" width="28" height="34" rx="2"/><path d="M3 36 l4 3 h24"/>
    <text x="7" y="14" font-size="10" fill="var(--orange)" stroke="none" font-family="Arimo,sans-serif" font-weight="700">$</text>
    <path d="M15 8h12M15 13h12M7 20h20M7 28l6-5 5 5 8-6"/>
  </svg>
  <article class="column col-1">
    <h2>Lorem ipsum dolor sit amet, consectetur adipiscing elit.</h2>
    <p>In lacinia semper justo vitae laoreet. Sed a scelerisque dui. Sed auctor, elit sed faucibus maximus, enim arcu euismod ipsum, sed dignissim justo felis in nibh.</p>
    <p>Vestibulum ante ipsum primis in faucibus orci luctus et ultrices posuere cubilia curae; Phasellus lobortis nisl vestibulum pretium ullamcorper. Nulla erat tellus, finibus elementum venenatis vitae, laoreet et nibh.</p>
    <p>Quisque vulputate gravida tellus et scelerisque. Quisque sagittis, nibh auctor tincidunt fermentum, nunc risus sagittis tortor, sed porttitor mi neque quis orci. Mauris sit amet purus vel justo porta fermentum id non ante.</p>
  </article>

  <svg class="icon" style="left:263px;top:758px" width="40" height="34" viewBox="0 0 40 34" fill="none" stroke="var(--orange)" stroke-width="1.8">
    <rect x="4" y="2" width="32" height="24" rx="1.5"/><path d="M1 28h38l-2 3H3z"/>
    <path d="M9 21l7-7 5 4 9-9"/>
  </svg>
  <article class="column col-2">
    <p>Lorem ipsum dolor sit amet, consectetur adipiscing elit. In lacinia semper justo vitae laoreet. Sed a scelerisque dui. Sed auctor, elit sed faucibus maximus, enim arcu euismod ipsum, sed dignissim justo felis in nibh.</p>
    <h2>Vestibulum ante ipsum primis in faucibus orci luctus et ultrices posuere cubili.</h2>
    <p>Phasellus lobortis nisl vestibulum pretium ullamcorper. Nulla erat tellus, finibus elementum venenatis vitae, laoreet et nibh.</p>
    <p>Quisque vulputate gravida tellus et scelerisque. Quisque sagittis, nibh auctor tincidunt fermentum, nunc risus sagittis tortor, sed porttitor mi neque quis orci. Mauris sit amet purus vel justo.</p>
  </article>

  <svg class="icon" style="left:494px;top:642px" width="36" height="40" viewBox="0 0 36 40" fill="none" stroke="var(--orange)" stroke-width="2">
    <path d="M11 3h14l-4 8h-6z"/><path d="M15 11C5 16 2 24 3 31c1 5 5 7 15 7s14-2 15-7c1-7-2-15-12-20"/>
    <text x="13" y="32" font-size="15" fill="var(--orange)" stroke="none" font-family="Arimo,sans-serif" font-weight="700">$</text>
  </svg>
  <article class="column col-3">
    <h2>Lorem ipsum dolor sit amet, consectetur adipiscing elit.</h2>
    <p>In lacinia semper justo vitae laoreet. Sed a scelerisque dui. Sed auctor, elit sed faucibus maximus, enim arcu euismod ipsum, sed dignissim justo felis in nibh.</p>
    <p>Vestibulum ante ipsum primis in faucibus orci luctus et ultrices posuere cubilia curae; Phasellus lobortis nisl vestibulum pretium ullamcorper. Nulla erat tellus, finibus elementum venenatis vitae, laoreet et nibh.</p>
    <p>Quisque vulputate gravida tellus et scelerisque. Quisque sagittis, nibh auctor tincidunt fermentum, nunc risus sagittis tortor, sed porttitor mi neque quis orci. Mauris sit amet purus vel justo porta fermentum id non ante.</p>
  </article>

  <footer>
    <div aria-label="Professional body memberships">
      <div class="badge" style="left:70px;top:997px;width:51px;height:22px"></div>
      <div class="badge" style="left:148px;top:990px;width:53px;height:36px"></div>
      <div class="badge" style="left:229px;top:992px;width:56px;height:34px"></div>
      <div class="badge" style="left:306px;top:988px;width:68px;height:38px"></div>
      <div class="badge" style="left:395px;top:993px;width:63px;height:30px;border-radius:15px"></div>
      <div class="badge" style="left:486px;top:986px;width:22px;height:44px"></div>
    </div>
    <div class="legal">
      <i>Meridian Advisory Pty Limited Business, Financial &amp; Wealth Advisors</i>
      <b>ACN 000555321</b>
    </div>
    <div class="base-bar"></div>
  </footer>
</main>
</body>
</html>
```